Website for Company that serves and supports Investment Banks

We are seeking to have a six page website that provides a basic description of our company's services. Our company provides Financial Models and Investment Memos on an outsourced basis to Small Investment Banks and Investment firms. We do not require a shopping cart. We already have a logo attached.

Target Market(s)

Small, regional investment banks. Small private equity firms.

Industry/Entity Type

Finance And Accounting

Coding

Coded - Design and coding required

Number of Pages Required

5+ page

Requirements
Nice to have
• Please use the logo design to drive how you design the layout for the website

```html
<!DOCTYPE html>
<html lang="en">
<head>
<meta charset="utf-8">
<title>Why Hire Us? – Ledgerline Analyst</title>
<link rel="stylesheet" href="https://fonts.googleapis.com/css2?family=Montserrat:wght@100;200;400;500;600;700&display=swap">
<style>
  :root {
    --navy: #0b4a88;
    --icon-blue: #1a5a98;
    --band-gray: #55565a;
    --text-gray: #555;
    --title-ink: #1e1e22;
    --white: #fff;
    --black: #000;
  }
  * { box-sizing: border-box; margin: 0; padding: 0; }
  html, body { width: 1200px; height: 2707px; overflow: hidden; background: var(--white); }
  body { position: relative; font-family: "Montserrat", Arial, sans-serif; }

  .main-nav {
    position: absolute; top: 0; left: 0; width: 1200px; height: 61px;
    background: var(--navy); z-index: 3;
  }
  .main-nav a {
    position: absolute; top: 0; line-height: 61px; color: var(--white);
    font-size: 23px; font-weight: 400; text-decoration: none;
    transform: translateX(-50%); white-space: nowrap;
  }
  .main-nav a.is-current { font-weight: 700; }

  .hero { position: absolute; top: 61px; left: 0; width: 1200px; height: 620px; }
  .hero svg { position: absolute; inset: 0; }
  .hero-title {
    position: absolute; left: 94px; top: 62px; font-weight: 100;
    font-size: 92px; line-height: 110px; letter-spacing: 4px;
    color: var(--title-ink); text-transform: uppercase;
  }

  .reason { position: absolute; left: 0; width: 1200px; text-align: center; }
  .reason-icon { position: absolute; left: 575px; width: 50px; height: 50px; }
  .reason-text {
    position: absolute; left: 140px; width: 920px; color: var(--text-gray);
    font-size: 26px; line-height: 31px; font-weight: 400; text-align: center;
  }
  .bullet-dot {
    position: absolute; left: 139px; width: 4px; height: 4px;
    border-radius: 50%; background: var(--text-gray);
  }

  .site-footer {
    position: absolute; top: 2426px; left: 0; width: 1200px; height: 234px;
    background: var(--navy); color: var(--white);
  }
  .footer-links { position: absolute; left: 40px; top: 37px; list-style: none; }
  .footer-links li { font-size: 19px; line-height: 29.5px; text-transform: uppercase; }
  .footer-contact { position: absolute; left: 821px; top: 40px; font-size: 18.5px; line-height: 22px; }
  .company-name { font-weight: 600; font-size: 18px; letter-spacing: 0.5px; text-transform: uppercase; }
  .contact-gap { height: 22px; }
  .pin-icon { position: absolute; left: 748px; top: 62px; width: 38px; height: 56px; }
  .copyright-bar {
    position: absolute; top: 2660px; left: 0; width: 1200px; height: 47px;
    background: var(--black); color: var(--white); text-align: center;
    font-size: 18px; line-height: 47px;
  }
</style>
</head>
<body>

<nav class="main-nav">
  <a style="left:137px">Home</a>
  <a style="left:329px">Services</a>
  <a style="left:516px">Leadership</a>
  <a class="is-current" style="left:706px">Why us?</a>
  <a style="left:892px">Our Process</a>
  <a style="left:1079px">Contact Us</a>
</nav>

<header class="hero">
  <svg width="1200" height="620" viewBox="0 0 1200 620">
    <defs>
      <linearGradient id="hero-tone" x1="0" y1="0" x2="1" y2="0.4">
        <stop offset="0" stop-color="#eef2f6"/>
        <stop offset="0.45" stop-color="#a9b7c6"/>
        <stop offset="0.75" stop-color="#c9d4df"/>
        <stop offset="1" stop-color="#e8edf2"/>
      </linearGradient>
    </defs>
    <path d="M0,372 Q560,790 1200,440 L1200,470 Q560,830 0,388 Z" fill="var(--navy)"/>
    <path d="M0,352 Q560,770 1200,422 L1200,446 Q560,800 0,372 Z" fill="var(--band-gray)"/>
    <path role="img" aria-label="Photo of two businessmen shaking hands in a bright office"
          d="M0,0 H1200 V426 Q560,772 0,354 Z" fill="url(#hero-tone)"/>
  </svg>
  <h1 class="hero-title">Why<br>Hire<br>Us?</h1>
</header>

<section class="reasons">
  <svg class="reason-icon" style="top:731px" viewBox="0 0 50 50">
    <text x="25" y="43" text-anchor="middle" font-family="Montserrat, sans-serif" font-weight="700" font-size="48" fill="var(--icon-blue)">$</text>
  </svg>
  <p class="reason-text" style="top:815px">We are much more cost-effective than hiring full-time Analyst pool.</p>

  <svg class="reason-icon" style="top:914px" viewBox="0 0 50 50">
    <rect x="3" y="4" width="44" height="42" rx="3" fill="none" stroke="var(--icon-blue)" stroke-width="4"/>
    <line x1="25" y1="4" x2="25" y2="46" stroke="var(--icon-blue)" stroke-width="4"/>
    <line x1="3" y1="11" x2="47" y2="11" stroke="var(--icon-blue)" stroke-width="4"/>
  </svg>
  <p class="reason-text" style="top:996px">We give You the ability to purchase Financial Models and Investment Memos on a “product-by-product” on demand basis with standardized prices.</p>

  <svg class="reason-icon" style="top:1154px" viewBox="0 0 50 50">
    <rect x="2" y="10" width="46" height="30" rx="3" fill="var(--icon-blue)"/>
    <rect x="8" y="15" width="34" height="20" rx="2" fill="var(--white)"/>
    <circle cx="25" cy="25" r="8" fill="var(--icon-blue)"/>
    <text x="25" y="30" text-anchor="middle" font-family="Montserrat, sans-serif" font-weight="700" font-size="12" fill="var(--white)">1</text>
  </svg>
  <p class="reason-text" style="top:1236px">Cost of our Financial Models and Investment Memos is less expensive than other outsourced deal providers including investment bankers, attorneys, accountants and industry consultants.</p>

  <svg class="reason-icon" style="top:1390px" viewBox="0 0 50 50">
    <rect x="3" y="7" width="44" height="36" rx="3" fill="none" stroke="var(--icon-blue)" stroke-width="4"/>
    <rect x="3" y="14" width="44" height="7" fill="var(--icon-blue)"/>
    <line x1="10" y1="34" x2="20" y2="34" stroke="var(--icon-blue)" stroke-width="3"/>
    <line x1="24" y1="34" x2="30" y2="34" stroke="var(--icon-blue)" stroke-width="3"/>
  </svg>
  <p class="reason-text" style="top:1472px">Cost of our Financial Models and Investment Memos is less expensive than Quality of Earnings Analysis reports provided by accounting firms.</p>

  <svg class="reason-icon" style="top:1630px" viewBox="0 0 50 50">
    <path d="M25,3 L47,13 V17 H3 V13 Z" fill="var(--icon-blue)"/>
    <rect x="6" y="19" width="5" height="20" fill="var(--icon-blue)"/>
    <rect x="16" y="19" width="5" height="20" fill="var(--icon-blue)"/>
    <rect x="29" y="19" width="5" height="20" fill="var(--icon-blue)"/>
    <rect x="39" y="19" width="5" height="20" fill="var(--icon-blue)"/>
    <rect x="3" y="41" width="44" height="6" fill="var(--icon-blue)"/>
  </svg>
  <p class="reason-text" style="top:1714px">We provide smaller, regional investment banks and private equity firms to outsource a large portion of their back-office in order to focus more time on marketing for new clients, executing deals and industry networking.</p>

  <svg class="reason-icon" style="top:1899px" viewBox="0 0 50 50">
    <path d="M40,14 A18,18 0 1 0 43,30" fill="none" stroke="var(--icon-blue)" stroke-width="7"/>
    <path d="M47,4 V22 H29 Z" fill="var(--icon-blue)"/>
  </svg>
  <p class="reason-text" style="top:1983px">Most Investment Banking Financial Analysts are “temporary two-year hires” which means constant employee turnover, ongoing recruitment, interviewing and training new Analysts that don’t stay with the company beyond two years.</p>

  <svg class="reason-icon" style="top:2192px" viewBox="0 0 50 50">
    <circle cx="25" cy="25" r="20" fill="none" stroke="var(--icon-blue)" stroke-width="5"/>
    <path d="M25,13 V26 H34" fill="none" stroke="var(--icon-blue)" stroke-width="4"/>
  </svg>
  <span class="bullet-dot" style="top:2286px"></span>
  <p class="reason-text" style="top:2272px">We are highly responsive and expedient.&nbsp; We deliver Financial Models and Investment Memos in 72 hours or less.</p>
</section>

<footer class="site-footer">
  <ul class="footer-links">
    <li>Home</li>
    <li>Services</li>
    <li>Leadership</li>
    <li>Why us?</li>
    <li>Our Process</li>
    <li>Contact Us</li>
  </ul>
  <svg class="pin-icon" viewBox="0 0 38 56">
    <path d="M19,2 C9,2 2,9.5 2,19 C2,32 19,54 19,54 C19,54 36,32 36,19 C36,9.5 29,2 19,2 Z" fill="var(--white)"/>
    <circle cx="19" cy="19" r="7" fill="var(--navy)"/>
  </svg>
  <address class="footer-contact" style="font-style:normal">
    <div class="company-name">Ledgerline Analyst.com</div>
    <div>412 Harborview Avenue</div>
    <div>Suite 14-220</div>
    <div>Easton, MA 02356</div>
    <div class="contact-gap"></div>
    <div>Phone: 555-014-2290</div>
    <div>Email: info@ledgerlineanalyst.com</div>
  </address>
</footer>
<div class="copyright-bar">© LEDGERLINEANALYST.COM 2018. All rights reserved.</div>

</body>
</html>
```